Halvorsen Partners Business Card

Halvorsen Partners Civil Construction
Marcus Halvorsen
CEO
727-518-6094
Marcus@HalvorsenSiteworks.example
www.HalvorsenSiteworks.example
Site Development
Utility Construction
Excavation
40876 County Lane 19
Land O' Lakes, FL 34638

Target Market(s)

Construction and government

Industry/Entity Type

Business

Contact Information for Business Card

I want an unique design that make a statement

Number of Pages Required

1 page

Font styles to use

Colors

Designer to choose colors to be used in the design.

Requirements
Must have
• unique design, feel free to modify or change the color of my logo.
Nice to have
• extra design features like spot UV, foil accents, color edges, unique paper, or any thing that would make my card pop.
• I like the feel of the image that I attached

```html
<!DOCTYPE html>
<html lang="en">
<head>
<meta charset="utf-8">
<title>Halvorsen Partners Business Card</title>
<link rel="stylesheet" href="https://fonts.googleapis.com/css2?family=Josefin+Sans:wght@400;600;700&family=Montserrat:wght@600;700&family=PT+Serif&display=swap">
<style>
  :root {
    --stage: #dfe8ea;
    --card: #000000;
    --sky: #cfe2e2;
    --haze: #6f7d80;
    --brand: #7a7ec4;
    --ink: #ffffff;
    --rule: #cfd4d6;
  }
  * { margin: 0; padding: 0; box-sizing: border-box; }
  html, body { width: 1200px; height: 808px; overflow: hidden; }
  body {
    background: var(--stage);
    display: flex;
    flex-direction: column;
    align-items: center;
    justify-content: center;
    gap: 44px;
    font-family: "Josefin Sans", sans-serif;
    color: var(--ink);
  }
  .card { width: 580px; }
  .card__scene {
    height: 92px;
    background: linear-gradient(180deg, var(--sky) 0%, var(--haze) 50%, var(--card) 100%);
  }
  .card__body {
    background: var(--card);
    height: 250px;
    padding: 22px 34px;
  }
  .lockup { display: flex; align-items: center; gap: 14px; }
  .lockup__mark { width: 54px; height: 54px; border: 3px solid var(--rule); flex: none; }
  .lockup__rule { width: 1px; height: 66px; background: var(--rule); flex: none; }
  .lockup__name { text-transform: uppercase; line-height: 1.15; }
  .lockup__name .line1 { display: block; font-size: 30px; font-weight: 600; letter-spacing: 0.5px; color: var(--brand); }
  .lockup__name .line2 { display: block; font-size: 21px; font-weight: 400; letter-spacing: 3.5px; color: var(--ink); }
  .card--front .lockup { margin-left: 62px; }
  .contact {
    text-align: center;
    margin-top: 26px;
    font-family: "Montserrat", sans-serif;
    font-weight: 600;
    letter-spacing: 2px;
    line-height: 1.55;
    font-size: 13px;
  }
  .contact__name { font-size: 16px; letter-spacing: 4px; font-weight: 700; }
  .services {
    list-style: none;
    margin-top: 16px;
    font-family: "Montserrat", sans-serif;
    font-weight: 700;
    font-size: 14px;
    letter-spacing: 1.8px;
    line-height: 1.45;
  }
  .services li::before { content: "\25CF"; margin-right: 8px; }
  .address { font-family: "PT Serif", serif; font-size: 15px; letter-spacing: 1px; line-height: 1.4; margin-top: 8px; }
  .web { font-family: "Montserrat", sans-serif; font-weight: 700; font-size: 13px; letter-spacing: 2px; margin-top: 8px; }
</style>
</head>
<body>
  <section class="card card--front">
    <div class="card__scene" role="img" aria-label="Silhouettes of a bulldozer, excavator and dump truck on a rough ground line against a pale sky"></div>
    <div class="card__body">
      <div class="lockup">
        <span class="lockup__mark"></span>
        <span class="lockup__rule"></span>
        <span class="lockup__name"><span class="line1">Halvorsen Partners</span><span class="line2">Civil Construction</span></span>
      </div>
      <div class="contact">
        <p class="contact__name">MARCUS HALVORSEN</p>
        <p>CEO</p>
        <p>727-518-6094</p>
        <p>Marcus@HalvorsenSiteworks.example</p>
      </div>
    </div>
  </section>

  <section class="card card--back">
    <div class="card__scene" role="img" aria-label="Silhouettes of a dump truck, excavator and bulldozer on a rough ground line against a pale sky"></div>
    <div class="card__body">
      <div class="lockup">
        <span class="lockup__name"><span class="line1">Halvorsen Partners</span><span class="line2">Civil Construction</span></span>
        <span class="lockup__rule"></span>
        <span class="lockup__mark"></span>
      </div>
      <ul class="services">
        <li>Site Development</li>
        <li>Utility Construction</li>
        <li>Excavation</li>
      </ul>
      <p class="address">40876 County Lane 19<br>Land O' Lakes, FL 34638</p>
      <p class="web">www.HalvorsenSiteworks.example</p>
    </div>
  </section>
</body>
</html>
```